Disposable Mini Sauce Pot Design for Asian Chain Food Brands

We operate a Hainan Chicken Rice takeout brand under the name Wokly8, with our official website: www.Wokly8.com.
We offer four signature house sauces and are launching brand-new packaging for our sauce line. We require custom graphic designs exclusively for the sauce cup lids.
Product Material & Base Specs
The sauce cups are made of PP plastic, available in two translucent base options: Translucent White and Translucent Orange.
Four Sauce Varieties for Individual Lid Designs
1. Red Sauce – Fried Sweet Chili Sauce
2.Green Sauce – Scallion Oil Dressing
3.Sweet Soy Sauce
4.Sweet Red Sauce (Special for Fried Chicken)
Differentiate each sauce lid design through unique graphics, typography, or illustrative elements for easy customer identification.
The marking NET WT 2 OZ must be clearly printed on every lid.
**There is no need to print full descriptive text or the full name of the sauces on each lid; the design only needs to clearly differentiate the four sauce varieties.
**Please reference the original design style and brand color palette shown on our official website, and feel free to fully unleash your creativity.
Look and feel
Each slider illustrates characteristics of the customer's brand and the style your logo design should communicate.

```html
<!DOCTYPE html>
<html lang="en">
<head>
<meta charset="utf-8">
<title>Wokly8 – Disposable Mini Sauce Pot Design</title>
<link href="https://fonts.googleapis.com/css2?family=Bebas+Neue&family=Anton&family=Montserrat:wght@400;500&family=Kaushan+Script&display=swap" rel="stylesheet">
<style>
  :root{
    --board-orange:#f4500a;
    --panel-white:#ffffff;
    --title-red:#8a0f05;
    --subtitle-green:#1f6b1f;
    --label-red:#8a1206;
    --label-green:#1f5a10;
    --label-brown:#2e1206;
    --pot-orange:#f6a36c;
    --pot-white:#eeeeee;
    --chili-bg:#e8400f;
    --chili-dark:#b3160a;
    --green-bg:#b6d12a;
    --green-dark:#1d5b1a;
    --soy-bg:#3a1e0c;
    --soy-accent:#c8651e;
    --sweet-bg:#e84a10;
    --sweet-dark:#a8130c;
    --white:#ffffff;
  }
  *{box-sizing:border-box;margin:0;padding:0}
  html,body{width:1200px;height:784px;overflow:hidden;background:var(--panel-white)}
  .board{position:relative;width:1200px;height:784px;overflow:hidden}
  .board__stage{position:absolute;left:0;top:0;width:965px;height:784px;background:var(--board-orange)}
  .board__panel{position:absolute;left:965px;top:0;width:235px;height:784px;background:var(--panel-white)}

  .headline{position:absolute;left:100px;top:18px;font-family:"Bebas Neue",sans-serif;font-size:92px;line-height:1;color:var(--title-red);letter-spacing:1px}
  .subhead{position:absolute;left:200px;top:110px;font-family:"Montserrat",sans-serif;font-weight:500;font-size:20px;letter-spacing:.5px;color:var(--subtitle-green)}

  .caption{position:absolute;text-align:center;transform:translateX(-50%);white-space:nowrap}
  .caption__script{font-family:"Kaushan Script",cursive;font-size:30px;line-height:1.1;display:block}
  .caption__note{font-family:"Montserrat",sans-serif;font-size:15px;color:#3a1005;display:block;margin-top:2px}
  .caption--red .caption__script{color:var(--label-red)}
  .caption--green .caption__script{color:var(--label-green)}
  .caption--soy .caption__script{color:var(--label-brown)}
  .caption--sweet .caption__script{color:var(--label-red)}
  .caption--sweet .caption__note{font-size:11px;color:var(--label-red)}

  .dots{position:absolute;display:grid;grid-template-columns:repeat(2,11px);gap:10px 14px}
  .dots span{width:11px;height:11px;border-radius:50%;background:var(--title-red)}

  .arrows{position:absolute;left:0;top:0}

  .pot{position:absolute;width:256px;height:246px;border-radius:30px;padding:20px;box-shadow:0 8px 14px rgba(80,20,0,.35)}
  .pot--orange{background:var(--pot-orange)}
  .pot--white{background:var(--pot-white)}
  .pot .lid{width:100%;height:100%;border-radius:18px}

  .tile{position:absolute;left:998px;width:168px;height:160px;box-shadow:6px 6px 8px rgba(0,0,0,.3);border-radius:18px}
  .tile .lid{width:100%;height:100%;border-radius:18px}

  .lid{position:relative;overflow:hidden;container-type:inline-size;color:var(--white)}
  .lid__brand{position:absolute;top:6%;left:0;right:0;text-align:center;line-height:.9}
  .lid__name{display:block;font-family:"Bebas Neue",sans-serif;font-size:15cqw;color:var(--white)}
  .lid__tag{display:block;font-family:"Montserrat",sans-serif;font-size:3cqw;font-weight:500;color:var(--white);margin-top:.5cqw}
  .lid__art{position:absolute}
  .lid__title{position:absolute;z-index:2;font-family:"Anton",sans-serif;font-weight:400;line-height:.95;text-transform:uppercase;white-space:nowrap}
  .lid__title span{display:block}
  .lid__net{position:absolute;z-index:2;left:25%;width:50%;bottom:6%;height:11%;display:flex;align-items:center;justify-content:center;font-family:"Bebas Neue",sans-serif;font-size:8cqw;color:var(--white);border-radius:2cqw}

  .lid--chili{background:linear-gradient(160deg,var(--chili-bg) 0 30%,var(--chili-dark) 30% 55%,var(--chili-bg) 55%)}
  .lid--chili .lid__title{left:7%;top:36%;font-size:21cqw}
  .lid--chili .lid__art{left:62%;top:30%;width:32%;height:52%;border-radius:40% 60% 30% 70%;background:linear-gradient(160deg,#ff8a1e,#e0350a)}
  .lid--chili .lid__net{background:var(--chili-dark)}

  .lid--green{background:linear-gradient(165deg,var(--green-bg) 0 35%,#9dbb1c 35% 60%,var(--green-bg) 60%)}
  .lid--green .lid__title{left:6%;top:33%;color:var(--green-dark)}
  .lid--green .lid__title .t-small{font-size:10cqw;line-height:1}
  .lid--green .lid__title .t-big{font-size:27cqw;line-height:1}
  .lid--green .lid__art{left:62%;top:26%;width:32%;height:56%;border-radius:50% 50% 40% 40%;background:linear-gradient(180deg,#e8f2a8,#ffffff)}
  .lid--green .lid__net{background:var(--green-dark)}

  .lid--soy{background:linear-gradient(160deg,var(--soy-bg) 0 35%,#24100a 35% 60%,var(--soy-bg) 60%)}
  .lid--soy .lid__art{left:18%;top:30%;width:64%;height:50%;border-radius:45% 55% 50% 50%;background:var(--soy-accent)}
  .lid--soy .lid__title{left:0;right:0;top:35%;text-align:center;color:var(--soy-bg)}
  .lid--soy .lid__title .t-small{font-size:9cqw;line-height:1}
  .lid--soy .lid__title .t-big{font-size:25cqw;line-height:1}
  .lid--soy .lid__net{background:#22100a}

  .lid--sweet{background:linear-gradient(160deg,var(--sweet-bg) 0 30%,var(--sweet-dark) 30% 58%,var(--sweet-bg) 58%)}
  .lid--sweet .lid__title{left:6%;top:26%}
  .lid--sweet .lid__title .t-small{font-size:11cqw;line-height:1}
  .lid--sweet .lid__title .t-big{font-size:30cqw;line-height:1}
  .lid--sweet .lid__art{left:64%;top:28%;width:30%;height:46%;border-radius:50% 50% 30% 60%;background:linear-gradient(160deg,#f28a3a,#d45a1a)}
  .lid__ribbon{position:absolute;z-index:3;left:6%;top:68%;background:var(--white);color:var(--sweet-dark);font-family:"Anton",sans-serif;font-size:5.5cqw;padding:.4cqw 2cqw;transform:rotate(-6deg);white-space:nowrap}
  .lid--sweet .lid__net{background:var(--sweet-dark)}
</style>
</head>
<body>
<main class="board">
  <div class="board__stage"></div>
  <div class="board__panel"></div>

  <h1 class="headline">DISPOSABLE MINI SAUCE</h1>
  <p class="subhead">POT DESIGN FOR ASIAN CHAIN FOOD BRANDS</p>

  <div class="caption caption--red" style="left:332px;top:158px"><span class="caption__script">Red Sauce</span><span class="caption__note">FRIED SWEET CHILI SAUCE</span></div>
  <div class="caption caption--green" style="left:610px;top:158px"><span class="caption__script">Green Sauce</span><span class="caption__note">SCALLION OIL DRESSING</span></div>
  <div class="caption caption--soy" style="left:107px;top:476px"><span class="caption__script">Sweet Soy</span><span class="caption__note">SAUCE</span></div>
  <div class="caption caption--sweet" style="left:832px;top:474px"><span class="caption__script">Sweet Red Sauce</span><span class="caption__note">SPECIAL FOR FRIED CHICKEN</span></div>

  <div class="dots" style="left:866px;top:138px"><span></span><span></span><span></span><span></span><span></span><span></span><span></span><span></span></div>
  <div class="dots" style="left:65px;top:652px"><span></span><span></span><span></span><span></span><span></span><span></span><span></span><span></span></div>

  <svg class="arrows" width="965" height="784" viewBox="0 0 965 784" aria-hidden="true">
    <g fill="none" stroke-width="3" stroke-linecap="round" stroke-linejoin="round">
      <path d="M187 211 C150 270 148 330 168 367" stroke="var(--label-red)"/>
      <path d="M156 352 L168 367 L176 349" stroke="var(--label-red)"/>
      <path d="M760 372 C800 320 805 262 775 212" stroke="var(--label-green)"/>
      <path d="M768 231 L775 212 L789 226" stroke="var(--label-green)"/>
      <path d="M187 734 C145 682 145 620 175 575" stroke="var(--label-brown)"/>
      <path d="M162 588 L175 575 L178 594" stroke="var(--label-brown)"/>
      <path d="M765 575 C805 622 805 690 777 734" stroke="var(--label-red)"/>
      <path d="M772 714 L777 734 L792 720" stroke="var(--label-red)"/>
    </g>
  </svg>

  <div class="pot pot--orange" style="left:205px;top:238px">
    <div class="lid lid--chili">
      <div class="lid__brand"><span class="lid__name">Wokly8</span><span class="lid__tag">HAINAN CHICKEN</span></div>
      <div class="lid__art" role="img" aria-label="Illustration of a red chili pepper with flames"></div>
      <div class="lid__title"><span>RED</span><span>CHILI</span></div>
      <div class="lid__net">NET WT 2 OZ</div>
    </div>
  </div>
  <div class="pot pot--white" style="left:485px;top:238px">
    <div class="lid lid--green">
      <div class="lid__brand"><span class="lid__name">Wokly8</span><span class="lid__tag">HAINAN CHICKEN</span></div>
      <div class="lid__art" role="img" aria-label="Illustration of green scallions with oil drops and a ripple"></div>
      <div class="lid__title"><span class="t-small">GREEN</span><span class="t-small">SCALLION</span><span class="t-big">OIL</span></div>
      <div class="lid__net">NET WT 2 OZ</div>
    </div>
  </div>
  <div class="pot pot--white" style="left:205px;top:503px">
    <div class="lid lid--soy">
      <div class="lid__brand"><span class="lid__name">Wokly8</span><span class="lid__tag">HAINAN CHICKEN</span></div>
      <div class="lid__art" role="img" aria-label="Illustration of an orange soy sauce splash"></div>
      <div class="lid__title"><span class="t-small">SWEET</span><span class="t-big">SOY</span></div>
      <div class="lid__net">NET WT 2 OZ</div>
    </div>
  </div>
  <div class="pot pot--orange" style="left:484px;top:503px">
    <div class="lid lid--sweet">
      <div class="lid__brand"><span class="lid__name">Wokly8</span><span class="lid__tag">HAINAN CHICKEN</span></div>
      <div class="lid__art" role="img" aria-label="Illustration of a fried chicken drumstick"></div>
      <div class="lid__title"><span class="t-small">SWEET</span><span class="t-big">RED</span></div>
      <div class="lid__ribbon">FOR FRIED CHICKEN</div>
      <div class="lid__net">NET WT 2 OZ</div>
    </div>
  </div>

  <div class="tile" style="top:34px">
    <div class="lid lid--chili">
      <div class="lid__brand"><span class="lid__name">Wokly8</span><span class="lid__tag">HAINAN CHICKEN</span></div>
      <div class="lid__art" role="img" aria-label="Illustration of a red chili pepper with flames"></div>
      <div class="lid__title"><span>RED</span><span>CHILI</span></div>
      <div class="lid__net">NET WT 2 OZ</div>
    </div>
  </div>
  <div class="tile" style="top:221px">
    <div class="lid lid--green">
      <div class="lid__brand"><span class="lid__name">Wokly8</span><span class="lid__tag">HAINAN CHICKEN</span></div>
      <div class="lid__art" role="img" aria-label="Illustration of green scallions with oil drops and a ripple"></div>
      <div class="lid__title"><span class="t-small">GREEN</span><span class="t-small">SCALLION</span><span class="t-big">OIL</span></div>
      <div class="lid__net">NET WT 2 OZ</div>
    </div>
  </div>
  <div class="tile" style="top:407px">
    <div class="lid lid--soy">
      <div class="lid__brand"><span class="lid__name">Wokly8</span><span class="lid__tag">HAINAN CHICKEN</span></div>
      <div class="lid__art" role="img" aria-label="Illustration of an orange soy sauce splash"></div>
      <div class="lid__title"><span class="t-small">SWEET</span><span class="t-big">SOY</span></div>
      <div class="lid__net">NET WT 2 OZ</div>
    </div>
  </div>
  <div class="tile" style="top:583px">
    <div class="lid lid--sweet">
      <div class="lid__brand"><span class="lid__name">Wokly8</span><span class="lid__tag">HAINAN CHICKEN</span></div>
      <div class="lid__art" role="img" aria-label="Illustration of a fried chicken drumstick"></div>
      <div class="lid__title"><span class="t-small">SWEET</span><span class="t-big">RED</span></div>
      <div class="lid__ribbon">FOR FRIED CHICKEN</div>
      <div class="lid__net">NET WT 2 OZ</div>
    </div>
  </div>
</main>
</body>
</html>
```